Locksmiths Business Card Designs needed!!

I need a business card design for my new small locksmith business.
I would love my business card to be simple, (not too many photos of locks or keys) but strong images so that everyone can recognise it is locksmithing business without reading the words.

I want all information i put in upper article to appear on front side in anyway depending on your design of suggestions and on the back side I would love to mention theses;
-24 /7 mobile services (including weekends & public holidays)
-Residential / Commercial/ Automotive
-Opening / Repair / Installation
-Cut keys

Im not a native english speaker so you can fix the words or expressions as you think it is right and natural.

I realised that in the business names, there is too many "locks" and "s" so I would love to seperate the words somehow so that it is more natural when someone read the business name on the card. for example,put the part of "Bright Harbour Trade Services" first line and the part of "Locksmiths" on the other line....I am just suggesting..doesn't need to be like that..but it should say "Locksmiths" as it is locksmiths business. :)

Target Market(s)

all generations

Industry/Entity Type

Locksmith

Contact Information for Business Card

business name : Bright Harbour Trade Services Locksmiths
ABN 46281903754
Name : Tom Reyes (바다 문)
phone : 0468 219 357
email : brightharbourtrade@mailvero.net

Requirements
Must have
• A symbol of either a key or a lock
Nice to have
• I like the symbol of a key in the photo I have attached here. So maybe, if you couldn't find any other good symbols I am happy to have the symbol on the business somehow.
Should not have
• Too many keys or locks

```html
<!DOCTYPE html>
<html lang="en">
<head>
<meta charset="utf-8">
<title>Bright Harbour Trade Services Locksmiths – Business Card</title>
<link rel="stylesheet" href="https://fonts.googleapis.com/css2?family=Arimo&family=Noto+Sans+KR&family=Open+Sans:ital,wght@0,400;0,700;1,700&display=swap">
<style>
  :root {
    --page: #ffffff;
    --card-white: #ffffff;
    --charcoal: #3d3c3f;
    --accent-blue: #00aeef;
    --text-light: #ffffff;
    --text-dark: #3d3c3f;
  }
  * { margin: 0; padding: 0; box-sizing: border-box; }
  html, body { width: 1200px; height: 900px; overflow: hidden; background: var(--page); }
  .canvas { position: relative; width: 1200px; height: 900px; font-family: "Open Sans", sans-serif; }

  .card { position: absolute; overflow: hidden; box-shadow: 0 2px 6px rgba(0,0,0,0.35); }
  .card-front { left: 272px; top: 57px; width: 618px; height: 373px; background: var(--card-white); }
  .card-back { left: 272px; top: 474px; width: 621px; height: 376px; background: var(--charcoal); }

  .brand { position: absolute; display: flex; align-items: center; }
  .brand-dot { border-radius: 50%; flex: none; }
  .brand-name { font-weight: 700; line-height: 1.1; text-align: right; }
  .brand-name span { display: block; }

  .card-front .brand { left: 30px; top: 63px; }
  .card-front .brand-dot { width: 88px; height: 88px; background: var(--charcoal); margin-right: 24px; }
  .card-front .brand-name { color: var(--text-dark); font-size: 21px; }
  .card-front .brand-name .brand-trade { font-size: 25px; letter-spacing: 0.5px; }

  .abn { position: absolute; right: 28px; top: 164px; font-size: 16px; color: var(--text-dark); }
  .abn-label { color: var(--accent-blue); }

  .front-lower { position: absolute; left: 0; top: 191px; width: 100%; height: 182px; background: var(--charcoal); border-top: 8px solid var(--accent-blue); }
  .holder-name { position: absolute; left: 36px; top: 30px; font-family: "Arimo", "Noto Sans KR", sans-serif; font-size: 22px; color: var(--text-light); }
  .holder-name .holder-korean { font-family: "Noto Sans KR", sans-serif; font-size: 21px; }
  .contact { position: absolute; left: 32px; display: flex; align-items: center; font-size: 20px; color: var(--text-light); }
  .contact svg { margin-right: 8px; }
  .contact-phone { top: 96px; }
  .contact-email { top: 125px; }

  .card-back .brand { left: 41px; top: 41px; }
  .card-back .brand-dot { width: 64px; height: 64px; background: var(--text-light); margin-right: 16px; }
  .card-back .brand-name { color: var(--text-light); font-size: 16px; }
  .card-back .brand-name .brand-trade { font-size: 19px; letter-spacing: 0.4px; }

  .services { position: absolute; left: 40px; top: 214px; list-style: none; }
  .services li { position: relative; padding-left: 13px; font-size: 17px; font-weight: 700; font-style: italic; line-height: 23px; color: var(--text-light); }
  .services li::before { content: ""; position: absolute; left: 0; top: 9px; width: 5px; height: 5px; border-radius: 50%; background: var(--accent-blue); }

  .back-stripes { position: absolute; left: 0; bottom: 0; }
</style>
</head>
<body>
<main class="canvas">

  <section class="card card-front" aria-label="Card front">
    <div class="brand">
      <div class="brand-dot"></div>
      <div class="brand-name"><span>Bright Harbour Trade Services</span><span class="brand-trade">LOCKSMITHS</span></div>
    </div>
    <p class="abn"><span class="abn-label">ABN</span> 46281903754</p>
    <div class="front-lower">
      <p class="holder-name">Tom Reyes (<span class="holder-korean">바다 문</span>)</p>
      <p class="contact contact-phone">
        <svg width="12" height="12" viewBox="0 0 12 12" aria-hidden="true"><rect width="12" height="12" rx="2" fill="#00aeef"/><path d="M4 2.5 C3 3.5 3.2 6 5 7.8 C6.8 9.6 8.6 9.4 9.5 8.4 L8.2 7.2 L7.2 7.9 C6.2 7.3 4.8 5.9 4.2 4.9 L4.9 3.9 Z" fill="#3d3c3f"/></svg>
        0468 219 357
      </p>
      <p class="contact contact-email">
        <svg width="14" height="10" viewBox="0 0 14 10" aria-hidden="true"><rect width="14" height="10" fill="#00aeef"/><path d="M0.5 0.8 L7 5.5 L13.5 0.8" fill="none" stroke="#3d3c3f" stroke-width="1.2"/></svg>
        brightharbourtrade@mailvero.net
      </p>
    </div>
  </section>

  <section class="card card-back" aria-label="Card back">
    <div class="brand">
      <div class="brand-dot"></div>
      <div class="brand-name"><span>Bright Harbour Trade Services</span><span class="brand-trade">LOCKSMITHS</span></div>
    </div>
    <ul class="services">
      <li>24 /7 mobile services (including weekends &amp; public holidays)</li>
      <li>Residential / Commercial/ Automotive</li>
      <li>Opening / Repair / Installation</li>
      <li>Cut keys</li>
    </ul>
    <svg class="back-stripes" width="621" height="52" viewBox="0 0 621 52" aria-hidden="true">
      <polygon points="0,2 414,2 398,29 0,29" fill="#00aeef"/>
      <polygon points="414,8 621,8 621,35 398,35" fill="#ffffff"/>
    </svg>
  </section>

</main>
</body>
</html>
```